Design some Business Cards

Will leave good review!
I need business cards with a logo and contact information.
This company name is Tidewell Plumbing Corp. Its a new Massachusetts plumbing business. Tidewell is phone area code in Massachusetts. Results have to look professional and clean. Please submit business card examples and logo ideas.
I was thinking Tidewell being designed as digits on the phone keys. Try to use a black background(with decorations or not), the rest being gold. Try to do a double sided design. Just large logo on one side, same slightly smaller logo and contact information on the other.

Lets go, we are getting there! I really like your ideas so far, thank you, I have more work to be done!
I will leave a 5 star review to the winner!

```html
<!DOCTYPE html>
<html lang="en">
<head>
<meta charset="utf-8">
<title>Tidewell Plumbing Corp — Business Cards</title>
<link rel="stylesheet" href="https://fonts.googleapis.com/css2?family=Arimo:wght@400;700&display=swap">
<style>
  :root {
    --page-bg: #ecebe8;
    --gold-light: #f6efc4;
    --gold: #e9dca0;
    --gold-text: #eadb9a;
    --ink: #111111;
    --card-black: #050505;
    --shadow: rgba(0, 0, 0, 0.18);
  }
  * { box-sizing: border-box; margin: 0; padding: 0; }
  html, body {
    width: 1200px;
    height: 1200px;
    overflow: hidden;
    background: var(--page-bg);
    font-family: "Arimo", Arial, sans-serif;
  }
  .sheet {
    width: 1200px;
    height: 1200px;
    display: flex;
    flex-direction: column;
    align-items: center;
    justify-content: center;
    gap: 60px;
  }
  .card {
    position: relative;
    width: 840px;
    height: 480px;
    border-radius: 6px;
    box-shadow: 0 10px 28px var(--shadow);
    overflow: hidden;
  }

  /* Front side */
  .card--front {
    background: radial-gradient(ellipse at 50% 40%, var(--gold-light) 0%, var(--gold) 100%);
    display: flex;
    align-items: center;
    justify-content: center;
  }
  .brand {
    display: flex;
    align-items: center;
    gap: 28px;
  }
  .brand__dot {
    flex: none;
    border-radius: 50%;
  }
  .brand__name {
    font-weight: 700;
    line-height: 1.05;
  }
  .card--front .brand__dot {
    width: 96px;
    height: 96px;
    background: var(--ink);
  }
  .card--front .brand__name {
    color: var(--ink);
    font-size: 64px;
  }

  /* Back side */
  .card--back {
    background: var(--card-black);
  }
  .card--back .brand {
    position: absolute;
    top: 62px;
    left: 50%;
    transform: translateX(-50%);
    gap: 18px;
  }
  .card--back .brand__dot {
    width: 52px;
    height: 52px;
    background: var(--gold-text);
  }
  .card--back .brand__name {
    color: var(--gold-text);
    font-size: 34px;
  }
  .contact {
    position: absolute;
    top: 220px;
    left: 0;
    right: 0;
    text-align: center;
    color: var(--gold-text);
  }
  .contact__name {
    font-size: 44px;
    font-weight: 700;
    letter-spacing: 1px;
  }
  .contact__phone {
    margin-top: 14px;
    font-size: 26px;
    display: inline-flex;
    align-items: center;
    gap: 10px;
  }
  .contact__phone svg { width: 22px; height: 22px; }
  .web-band {
    position: absolute;
    left: 0;
    right: 0;
    bottom: 0;
    height: 66px;
    background: linear-gradient(90deg, var(--gold-light), var(--gold));
    display: flex;
    align-items: center;
    padding-left: 70px;
    gap: 14px;
    color: var(--ink);
    font-size: 22px;
  }
  .web-band svg { width: 28px; height: 28px; }
</style>
</head>
<body>
<main class="sheet">

  <section class="card card--front" aria-label="Card front">
    <div class="brand">
      <span class="brand__dot"></span>
      <span class="brand__name">Tidewell<br>Plumbing Corp</span>
    </div>
  </section>

  <section class="card card--back" aria-label="Card back">
    <div class="brand">
      <span class="brand__dot"></span>
      <span class="brand__name">Tidewell<br>Plumbing Corp</span>
    </div>

    <div class="contact">
      <p class="contact__name">DALE MERCER</p>
      <p class="contact__phone">
        <svg viewBox="0 0 24 24" aria-hidden="true">
          <path fill="currentColor" d="M6.6 10.8a15.1 15.1 0 0 0 6.6 6.6l2.2-2.2c.3-.3.7-.4 1-.2 1.1.4 2.3.6 3.6.6.6 0 1 .4 1 1V20c0 .6-.4 1-1 1A17 17 0 0 1 3 4c0-.6.4-1 1-1h3.5c.6 0 1 .4 1 1 0 1.3.2 2.5.6 3.6.1.3 0 .7-.2 1z"/>
        </svg>
        (555)014227
      </p>
    </div>

    <div class="web-band">
      <svg viewBox="0 0 24 24" aria-hidden="true" fill="none" stroke="currentColor" stroke-width="1.4">
        <circle cx="12" cy="12" r="10"/>
        <ellipse cx="12" cy="12" rx="4.5" ry="10"/>
        <line x1="2" y1="12" x2="22" y2="12"/>
        <path d="M4 6.5h16M4 17.5h16"/>
      </svg>
      <span class="web-band__url">www.tidewellplumbing.com</span>
    </div>
  </section>

</main>
</body>
</html>
```